Book Cover "Venice"

Creation of a cover (14 x 20.5 cm + bleed area) for a book:
Image: “BrumeVerte” (Tiff joined)
AUTHOR: Corinne Valmer
TITLE: The murmurs of Lorient
PUBLISHER: Editions Pluvane (AT THE BOTTOM OF THE COVER)

Target Market(s)

Readers of romantic novels

Industry/Entity Type

Book

```html
<!DOCTYPE html>
<html lang="en">
<head>
<meta charset="utf-8">
<title>The murmurs of Lorient — Corinne Valmer</title>
<link rel="stylesheet" href="https://fonts.googleapis.com/css2?family=Cinzel:wght@400;500&display=swap">
<style>
  :root {
    --page-bg: #e9e6e1;
    --sky-deep: #3a0a0c;
    --sky-crimson: #9e0f0e;
    --sky-red: #d8261a;
    --sky-ember: #e84a22;
    --cloud-shadow: rgba(60, 20, 24, 0.55);
    --cloud-glow: rgba(255, 96, 40, 0.55);
    --dusk-dark: #1a0c0c;
    --band-shade: rgba(24, 18, 18, 0.7);
    --foot-shade: #0d0909;
    --type-white: #ffffff;
    --type-soft: #e8dcd6;
  }
  * { margin: 0; padding: 0; box-sizing: border-box; }
  html, body {
    width: 1200px;
    height: 1200px;
    overflow: hidden;
    background: var(--page-bg);
  }
  .canvas {
    position: relative;
    width: 1200px;
    height: 1200px;
    display: flex;
    align-items: center;
    justify-content: center;
  }
  .cover {
    position: relative;
    width: 751px;
    height: 1100px;
    overflow: hidden;
    font-family: "Cinzel", "Times New Roman", serif;
    color: var(--type-white);
    text-transform: uppercase;
  }
  .cover-photo {
    position: absolute;
    inset: 0;
    background:
      radial-gradient(ellipse 420px 60px at 30% 500px, var(--cloud-shadow), transparent 70%),
      radial-gradient(ellipse 380px 50px at 75% 360px, var(--cloud-shadow), transparent 70%),
      radial-gradient(ellipse 500px 90px at 55% 640px, var(--cloud-glow), transparent 70%),
      radial-gradient(ellipse 460px 70px at 40% 760px, var(--cloud-glow), transparent 70%),
      radial-gradient(ellipse 600px 200px at 50% 960px, rgba(10, 6, 6, 0.75), transparent 75%),
      linear-gradient(180deg,
        var(--sky-deep) 0%,
        var(--sky-crimson) 14%,
        var(--sky-red) 36%,
        var(--sky-ember) 52%,
        var(--sky-red) 66%,
        #7a120f 80%,
        var(--dusk-dark) 90%,
        #0d0808 100%);
  }
  .title {
    position: absolute;
    top: 150px;
    left: 0;
    right: 0;
    text-align: center;
    font-weight: 400;
    line-height: 1;
    white-space: nowrap;
  }
  .title-line { display: block; }
  .title-line--small { font-size: 92px; letter-spacing: 1px; }
  .title-line--mid { font-size: 92px; margin-top: 6px; }
  .title-line--large { font-size: 126px; margin-top: 2px; }
  .author-band {
    position: absolute;
    left: 0;
    right: 0;
    top: 880px;
    height: 168px;
    background: var(--band-shade);
    display: flex;
    align-items: center;
    justify-content: center;
  }
  .author-name {
    font-size: 78px;
    font-weight: 400;
    line-height: 0.98;
    text-align: center;
    white-space: nowrap;
  }
  .publisher {
    position: absolute;
    left: 0;
    right: 0;
    bottom: 0;
    height: 52px;
    background: var(--foot-shade);
    display: flex;
    align-items: center;
    justify-content: center;
    font-size: 20px;
    letter-spacing: 4px;
    color: var(--type-soft);
  }
</style>
</head>
<body>
  <main class="canvas">
    <article class="cover">
      <div class="cover-photo" role="img" aria-label="Photograph: blazing red sunset sky with dark clouds over a city skyline of church domes and bell towers in silhouette, with lit street lanterns on the right"></div>
      <h1 class="title">
        <span class="title-line title-line--small">The</span>
        <span class="title-line title-line--mid">Murmurs of</span>
        <span class="title-line title-line--large">Lorient</span>
      </h1>
      <div class="author-band">
        <p class="author-name">Corinne<br>Valmer</p>
      </div>
      <p class="publisher">Editions Pluvane</p>
    </article>
  </main>
</body>
</html>
```